Symposium Flyer

I need a flyer for advertising an upcoming symposium titled, "Stirring and settling the chromatin code", I am organizing as well as a webpage design for the symposium. The Symposium is taking place on Thursday, February 7th, 2019 at the Valdmere University Harrowgate School of Medicine. It is being held by the Gene Regulation Centre at the Corvath Hall for Applied Discovery (Maplewick Auditorium and Lobby, 1275 Larkspur Terrace Way, Philadelphia, PA 19187). You can view previous symposiums from our institution at https://events.valdmere-med.example/generegulation/symposiums/

Our Keynote speakers for this symposium are:
Theodor Wallmark, M.D., Professor of Biology at the Ostrander Polytechnic Academy; Founding Member of the Brackenfield Foundation for Life Science Study; Member of the Council of Clinical Scholars.
AND
Martin (Marty) Okafor, M.D., President of the Quelvora Laboratories for Therapeutic Discovery (QLTD)

We will be adding 8 more speakers to this event, so please leave room for extra speakers to be added and for a website registration link and QR code to be added.

Please email me should have additional questions - torvik@mail.valdmere-med.example

```html
<!DOCTYPE html>
<html lang="en">
<head>
<meta charset="utf-8">
<title>Stirring and Settling the Chromatin Code — Symposium Flyer</title>
<link href="https://fonts.googleapis.com/css2?family=Exo+2:wght@800&family=Lato:wght@700;900&family=Tinos:ital,wght@0,700;1,400&display=swap" rel="stylesheet">
<style>
  :root {
    --red-top: #d8232a;
    --red-bottom: #7a0f16;
    --blue-top: #1f5fae;
    --blue-bottom: #1877c5;
    --navy: #1d4f9c;
    --link-blue: #1c6bb5;
    --ink: #333;
    --white: #fff;
    --paper-shade: #eeeff1;
    --footer-grey: #e6e7e9;
    --art-dark: #05060a;
  }
  * { margin: 0; padding: 0; box-sizing: border-box; }
  html, body { width: 907px; height: 1200px; overflow: hidden; }
  body { background: var(--white); font-family: "Lato", sans-serif; }

  .flyer {
    position: relative; width: 907px; height: 1200px; overflow: hidden;
    background: linear-gradient(90deg, var(--paper-shade) 0%, var(--white) 22%);
  }

  .hero-art { position: absolute; left: 0; top: 0; }

  .title-panel { position: absolute; left: 475px; top: 35px; width: 360px; }
  .event-title {
    font-family: "Exo 2", sans-serif; font-weight: 800; color: var(--white);
    font-size: 41px; line-height: 51px; text-transform: uppercase; margin: 58px 0 0 29px;
    letter-spacing: 0.3px;
  }
  .event-date, .event-host {
    color: var(--white); font-weight: 900; margin-left: 29px;
  }
  .event-date { font-size: 25px; line-height: 30px; margin-top: 25px; text-transform: uppercase; }
  .event-host { font-size: 24px; line-height: 30px; margin-top: 20px; }

  .venue {
    position: absolute; left: 504px; top: 580px; width: 320px;
    color: var(--white); font-weight: 700; font-size: 16.5px; line-height: 21px;
  }
  .venue p + p { margin-top: 21px; }

  .speakers { position: absolute; top: 630px; }
  .speakers.left { left: 70px; }
  .speakers.right { left: 476px; top: 781px; }
  .speaker { margin-bottom: 13px; }
  .speaker-name {
    display: flex; align-items: center; gap: 9px;
    font-family: "Tinos", serif; font-weight: 700; color: var(--link-blue); font-size: 19.5px; line-height: 24px;
  }
  .speaker-role {
    font-family: "Tinos", serif; font-style: italic; color: var(--ink);
    font-size: 10.2px; line-height: 13.5px; margin-left: 1px; margin-top: 2px;
  }
  .speaker-role.one-line { margin-bottom: 12px; }

  .footer-band { position: absolute; left: 0; top: 1071px; width: 907px; height: 129px; background: var(--footer-grey); }
  .footer-swoosh { position: absolute; left: 0; top: 1050px; }
  .partners {
    position: absolute; left: 350px; top: 1108px; width: 530px;
    display: flex; justify-content: space-between; align-items: center;
  }
  .partner { display: flex; align-items: center; gap: 9px; color: var(--navy); font-weight: 900; font-size: 17px; line-height: 20px; }
  .partner-mark { width: 14px; height: 14px; border-radius: 50%; background: var(--navy); flex: none; }
  .partner.school { width: 250px; }
</style>
</head>
<body>
<main class="flyer">

  <svg class="hero-art" width="907" height="760" viewBox="0 0 907 760" aria-hidden="true">
    <defs>
      <radialGradient id="moleculeGlow" cx="0.38" cy="0.45" r="0.55">
        <stop offset="0" stop-color="#4b3aa0"/>
        <stop offset="0.45" stop-color="#2c2f7a"/>
        <stop offset="0.8" stop-color="#0c1222"/>
        <stop offset="1" stop-color="#05060a"/>
      </radialGradient>
      <linearGradient id="redPanel" x1="0" y1="0" x2="0" y2="1">
        <stop offset="0" stop-color="#d8232a"/>
        <stop offset="0.55" stop-color="#8e1219"/>
        <stop offset="1" stop-color="#7a0f16"/>
      </linearGradient>
      <linearGradient id="bluePanel" x1="0" y1="0" x2="1" y2="1">
        <stop offset="0" stop-color="#1f5fae"/>
        <stop offset="1" stop-color="#1877c5"/>
      </linearGradient>
    </defs>
    <polygon points="37,35 869,35 869,474 37,556" fill="#05060a"/>
    <polygon points="37,35 475,35 475,512 37,556" fill="url(#moleculeGlow)" role="img" aria-label="Illustration of a chromatin molecule: DNA strands wrapped around histone proteins"/>
    <polygon points="475,35 835,35 835,478 475,543" fill="url(#redPanel)"/>
    <polygon points="475,547 835,512 835,741 475,741" fill="url(#bluePanel)"/>
    <circle cx="653" cy="532" r="43" fill="#fff"/>
    <polyline points="634,523 653,542 672,523" fill="none" stroke="#c8202a" stroke-width="9" stroke-linecap="round" stroke-linejoin="round"/>
  </svg>

  <header class="title-panel">
    <h1 class="event-title">Stirring &amp; Settling the Chromatin Code</h1>
    <p class="event-date">Thursday,<br>February 7th 2019</p>
    <p class="event-host">At The Valdmere University Harrowgate School Of Medicine</p>
  </header>

  <section class="venue">
    <p>Gene Regulation Centre At The Corvath Hall For Applied Discovery</p>
    <p>(Maplewick Auditorium And Lobby, 1275 Larkspur Terrace Way, Philadelphia, Pa 19187).</p>
  </section>

  <section class="speakers left">
    <article class="speaker">
      <h2 class="speaker-name"><svg width="22" height="22" viewBox="0 0 22 22" aria-hidden="true"><circle cx="11" cy="11" r="11" fill="#c8202a"/><polyline points="8.5,6 13.5,11 8.5,16" fill="none" stroke="#fff" stroke-width="3"/></svg>Theodor Wallmark, M.D.</h2>
      <p class="speaker-role">Professor of Biology at the Ostrander Polytechnic Academy;<br>Founding Member of the Brackenfield Foundation for Life Science Study;<br>Member of the Council of Clinical Scholars.</p>
    </article>
    <article class="speaker">
      <h2 class="speaker-name"><svg width="22" height="22" viewBox="0 0 22 22" aria-hidden="true"><circle cx="11" cy="11" r="11" fill="#c8202a"/><polyline points="8.5,6 13.5,11 8.5,16" fill="none" stroke="#fff" stroke-width="3"/></svg>Martin (Marty) Okafor, M.D.,</h2>
      <p class="speaker-role one-line">President of the Quelvora Laboratories for Therapeutic Discovery (QLTD)</p>
    </article>
    <article class="speaker">
      <h2 class="speaker-name"><svg width="22" height="22" viewBox="0 0 22 22" aria-hidden="true"><circle cx="11" cy="11" r="11" fill="#c8202a"/><polyline points="8.5,6 13.5,11 8.5,16" fill="none" stroke="#fff" stroke-width="3"/></svg>Name here name here</h2>
      <p class="speaker-role">Professor of Biology at the Ostrander Polytechnic Academy;<br>Founding Member of the Brackenfield Foundation for Life Science Study;<br>Member of the Council of Clinical Scholars.</p>
    </article>
    <article class="speaker">
      <h2 class="speaker-name"><svg width="22" height="22" viewBox="0 0 22 22" aria-hidden="true"><circle cx="11" cy="11" r="11" fill="#c8202a"/><polyline points="8.5,6 13.5,11 8.5,16" fill="none" stroke="#fff" stroke-width="3"/></svg>Name here name here</h2>
      <p class="speaker-role one-line">President of the Quelvora Laboratories for Therapeutic Discovery (QLTD)</p>
    </article>
    <article class="speaker">
      <h2 class="speaker-name"><svg width="22" height="22" viewBox="0 0 22 22" aria-hidden="true"><circle cx="11" cy="11" r="11" fill="#c8202a"/><polyline points="8.5,6 13.5,11 8.5,16" fill="none" stroke="#fff" stroke-width="3"/></svg>Name here name here</h2>
      <p class="speaker-role">Professor of Biology at the Ostrander Polytechnic Academy;<br>Founding Member of the Brackenfield Foundation for Life Science Study;<br>Member of the Council of Clinical Scholars.</p>
    </article>
    <article class="speaker">
      <h2 class="speaker-name"><svg width="22" height="22" viewBox="0 0 22 22" aria-hidden="true"><circle cx="11" cy="11" r="11" fill="#c8202a"/><polyline points="8.5,6 13.5,11 8.5,16" fill="none" stroke="#fff" stroke-width="3"/></svg>Name here name here</h2>
      <p class="speaker-role one-line">President of the Quelvora Laboratories for Therapeutic Discovery (QLTD)</p>
    </article>
  </section>

  <section class="speakers right">
    <article class="speaker">
      <h2 class="speaker-name"><svg width="22" height="22" viewBox="0 0 22 22" aria-hidden="true"><circle cx="11" cy="11" r="11" fill="#c8202a"/><polyline points="8.5,6 13.5,11 8.5,16" fill="none" stroke="#fff" stroke-width="3"/></svg>Name here name here</h2>
      <p class="speaker-role">Professor of Biology at the Ostrander Polytechnic Academy;<br>Founding Member of the Brackenfield Foundation for Life Science Study;<br>Member of the Council of Clinical Scholars.</p>
    </article>
    <article class="speaker">
      <h2 class="speaker-name"><svg width="22" height="22" viewBox="0 0 22 22" aria-hidden="true"><circle cx="11" cy="11" r="11" fill="#c8202a"/><polyline points="8.5,6 13.5,11 8.5,16" fill="none" stroke="#fff" stroke-width="3"/></svg>Name here name here</h2>
      <p class="speaker-role one-line">President of the Quelvora Laboratories for Therapeutic Discovery (QLTD)</p>
    </article>
    <article class="speaker">
      <h2 class="speaker-name"><svg width="22" height="22" viewBox="0 0 22 22" aria-hidden="true"><circle cx="11" cy="11" r="11" fill="#c8202a"/><polyline points="8.5,6 13.5,11 8.5,16" fill="none" stroke="#fff" stroke-width="3"/></svg>Name here name here</h2>
      <p class="speaker-role">Professor of Biology at the Ostrander Polytechnic Academy;<br>Founding Member of the Brackenfield Foundation for Life Science Study;<br>Member of the Council of Clinical Scholars.</p>
    </article>
    <article class="speaker">
      <h2 class="speaker-name"><svg width="22" height="22" viewBox="0 0 22 22" aria-hidden="true"><circle cx="11" cy="11" r="11" fill="#c8202a"/><polyline points="8.5,6 13.5,11 8.5,16" fill="none" stroke="#fff" stroke-width="3"/></svg>Name here name here</h2>
      <p class="speaker-role one-line">President of the Quelvora Laboratories for Therapeutic Discovery (QLTD)</p>
    </article>
  </section>

  <div class="footer-band"></div>
  <svg class="footer-swoosh" width="320" height="150" viewBox="0 0 320 150" aria-hidden="true">
    <defs>
      <linearGradient id="footerBlue" x1="0" y1="0" x2="1" y2="0">
        <stop offset="0" stop-color="#1877c5"/>
        <stop offset="1" stop-color="#1d4f9c"/>
      </linearGradient>
    </defs>
    <path d="M0,0 H235 Q268,0 277,28 L296,150 H0 Z" fill="url(#footerBlue)"/>
  </svg>

  <footer class="partners">
    <div class="partner"><span class="partner-mark"></span>Gene Regulation Centre</div>
    <div class="partner school"><span class="partner-mark"></span>Valdmere University Harrowgate School of Medicine</div>
  </footer>

</main>
</body>
</html>
```